Velvet And Fern - A music blogger named Dorian needs a website to combine all avenues of social media

I am a music blogger that is looking to create a website that becomes a one stop shop for my blog (www.dorianlasky.quillnest.com.au), Pagebook page, Tumbleleaf, Snapframe, upcoming events, Clipstream channel, Chirper, Photography by R.K.L. and potential future gigs DJ'ing.

I like the colours, black and white but am not opposed to a splash of colour somewhere or somehow. I would like to keep the appearance chic and clear.

My end design should be predominantly about my writing and upcoming events, i.e. my blog, with clear tabs on how to follow me by one of the above social media outlets.

Simple and chic is what comes to mind. Must include "Velvet & Fern" as the title please.

• I have uploaded a picture that is to be used for my biography.

```html
<!DOCTYPE html>
<html lang="en">
<head>
<meta charset="utf-8">
<title>Velvet &amp; Fern</title>
<link href="https://fonts.googleapis.com/css2?family=Ubuntu:wght@300;400;500;700&display=swap" rel="stylesheet">
<style>
:root{
  --ink:#000;
  --paper:#f4f4f4;
  --white:#fff;
  --footer:#141414;
  --muted:#bdbdbd;
  --grey:#8a8a8a;
  --rust:#7a3614;
  --orange:#f7941d;
  --cyan:#27b5e6;
  --icon:#9a9a9a;
}
*{margin:0;padding:0;box-sizing:border-box}
html,body{width:837px;height:1200px;overflow:hidden;background:var(--ink)}
body{font-family:"Ubuntu",sans-serif;color:var(--white);position:relative}
h1,h2,h3,h4{font-weight:400}
.abs{position:absolute}
.topbar{left:0;top:0;width:837px;height:40px;background:var(--paper);color:var(--ink)}
.masthead{position:absolute;left:87px;top:8px;height:22px;display:flex;align-items:center;gap:9px;white-space:nowrap}
.brand{font-weight:700;font-size:16px;letter-spacing:-.2px}
.brand-sep{width:2px;height:20px;background:var(--ink)}
.tagline{font-size:11.5px;padding-top:2px}
.nav{left:0;top:40px;width:837px;height:61px;background:var(--ink)}
.nav a{position:absolute;top:25px;font-size:13px;color:var(--muted);text-decoration:none;letter-spacing:.2px}
.nav a.active{color:var(--white)}
.nav .underline{position:absolute;left:330px;top:62px;width:57px;height:1px;border-top:1px dotted #888}
.hero{left:0;top:101px;width:837px;height:349px;background:var(--paper)}
.hero-photo{left:395px;top:101px;width:360px;height:349px;background:radial-gradient(ellipse at 55% 40%,#f2c15a 0%,#f1d7a0 35%,#f6ece0 65%,rgba(244,244,244,0) 85%)}
.welcome{left:99px;top:178px;font-size:28px;font-weight:300;color:var(--rust);letter-spacing:.2px}
.welcome-sub{left:103px;top:217px;width:310px;font-size:12.5px;line-height:15px;color:#333;font-weight:300}
.dots{left:103px;top:286px;display:flex;gap:3px}
.dots span{width:12px;height:12px;border-radius:50%;background:#2a2a2a}
.dots span.on{background:var(--orange)}
.section-title{font-size:27px;font-weight:300;letter-spacing:.3px}
.blog-title{left:98px;top:343px;color:var(--ink)}
.arrows{left:688px;top:351px;display:flex;gap:6px}
.arrows svg{display:block}
.card{top:382px;width:213px;height:180px;background:var(--ink)}
.card .photo{position:absolute;left:12px;top:10px;width:188px;height:188px;border-radius:50%;border:7px solid #2b2b2b}
.card-meta{top:580px;width:215px}
.card-meta .name{position:absolute;left:0;top:0;font-size:14px;font-weight:300}
.card-meta .link{position:absolute;left:108px;top:4px;font-size:9px;color:var(--cyan)}
.card-meta .desc{position:absolute;left:0;top:23px;font-size:9px;color:var(--muted);font-weight:300}
.card-meta .desc em{font-style:normal;color:var(--orange)}
.socials{top:628px;display:flex;gap:9px}
.socials span{width:20px;height:21px;background:var(--icon);color:var(--ink);font-size:8px;font-weight:700;display:flex;align-items:center;justify-content:center}
.socials span.first{background:#3b5b9a;color:var(--white)}
.rule{left:95px;top:660px;width:213px;border-top:1px dotted #777}
.video-title{left:97px;top:678px}
.bio-title{left:331px;top:678px}
.player{left:97px;top:722px;width:208px;height:130px;background:linear-gradient(160deg,#5a5a5a,#1e1e1e 70%)}
.player .bar{position:absolute;left:0;bottom:0;width:208px;height:16px;background:#111}
.player .track{position:absolute;left:43px;top:7px;width:105px;height:3px;background:#555}
.player .track i{display:block;width:52px;height:3px;background:#8cc63f}
.player .time{position:absolute;left:157px;top:4px;font-size:5px;color:#ccc}
.player .hd{position:absolute;left:176px;top:4px;font-size:5px;color:#cbe34a;font-weight:700}
.play{position:absolute;width:28px;height:28px;border-radius:50%;background:rgba(0,0,0,.35);display:flex;align-items:center;justify-content:center}
.thumb{top:861px;width:68px;height:102px;border:1px solid #555}
.bio-photo{left:318px;top:718px;width:214px;height:245px;background:linear-gradient(150deg,#9a9a9a,#3c3c3c 55%,#d0d0d0)}
.about{left:543px;top:716px;font-size:15px;font-weight:300;color:var(--orange)}
.about-text{left:541px;top:738px;width:204px;font-size:9.6px;line-height:11.7px;color:var(--muted);text-align:justify;font-weight:300}
.about-text p+p{margin-top:11px}
.about-text p.tight{margin-top:0}
.btn{left:541px;top:943px;width:66px;height:22px;background:var(--orange);color:var(--white);font-size:10.5px;display:flex;align-items:center;justify-content:center;border-radius:2px}
.footer{left:0;top:989px;width:837px;height:211px;background:var(--footer)}
.foot-title{top:1003px;font-size:14.5px;font-weight:400;letter-spacing:.2px}
.news{left:103px;width:210px}
.news .date{position:absolute;left:0;top:0;width:36px;height:36px;background:#2a2a2a;text-align:center;color:var(--muted)}
.news .date b{display:block;font-size:17px;font-weight:400;line-height:20px;margin-top:1px}
.news .date small{display:block;font-size:9px}
.news h4{position:absolute;left:48px;top:0;font-size:10px;font-weight:400}
.news p{position:absolute;left:48px;top:15px;width:160px;font-size:10px;line-height:21px;color:var(--muted)}
.links{left:331px;top:1037px;list-style:none}
.links li{font-size:10px;line-height:20.8px;padding-left:12px;position:relative}
.links li::before{content:"";position:absolute;left:0;top:8px;border-left:3px solid #aaa;border-top:2.5px solid transparent;border-bottom:2.5px solid transparent}
.news-input{left:547px;top:1035px;width:155px;height:22px;background:var(--white);border-radius:4px}
.go{left:708px;top:1034px;width:40px;height:24px;background:var(--orange);border-radius:4px;font-size:14px;display:flex;align-items:center;justify-content:center}
.subscribe{left:549px;top:1065px;font-size:9.5px;color:var(--muted)}
.follow{left:546px;top:1097px;font-size:14.5px;font-weight:400}
.follow-icons{left:546px;top:1126px;display:flex;gap:4px}
.follow-icons span{width:20px;height:20px;border-radius:50%;background:#555;color:#ddd;font-size:7px;display:flex;align-items:center;justify-content:center}
.follow-icons span.first{background:var(--cyan);color:var(--white)}
.copy{left:548px;top:1166px;font-size:9px}
</style>
</head>
<body>

<header class="abs topbar">
  <div class="masthead">
    <span class="brand">VELVET &amp; FERN.</span>
    <span class="brand-sep"></span>
    <span class="tagline">The musical ramblings of a boy named Dorian.</span>
  </div>
</header>

<nav class="abs nav">
  <a class="active" style="left:343px">HOME</a>
  <a style="left:415px">BIOGRAPHY</a>
  <a style="left:520px">PHOTOS</a>
  <a style="left:604px">VIDEOS</a>
  <a style="left:683px">CONTACTS</a>
  <span class="underline"></span>
</nav>

<section class="abs hero"></section>
<div class="abs hero-photo" role="img" aria-label="Portrait of a blonde singer in a cream gown with her name in script lettering"></div>
<h1 class="abs welcome">WELCOME LORIUM IPSUM</h1>
<p class="abs welcome-sub">Lorem Ipsum is simply dummy text of the printing and typesetting industry.</p>
<div class="abs dots"><span></span><span></span><span></span><span class="on"></span></div>

<h2 class="abs section-title blog-title">MY BLOG</h2>
<div class="abs arrows">
  <svg width="23" height="23" viewBox="0 0 23 23"><circle cx="11.5" cy="11.5" r="11.5" fill="#000"/><path d="M13.5 7v9l-6-4.5z" fill="#fff"/></svg>
  <svg width="23" height="23" viewBox="0 0 23 23"><circle cx="11.5" cy="11.5" r="11.5" fill="#000"/><path d="M9.5 7v9l6-4.5z" fill="#fff"/></svg>
</div>

<article class="abs card" style="left:95px"><div class="photo" role="img" aria-label="Album art of a singer with curly hair in warm sepia tones" style="background:radial-gradient(circle,#d48a45,#7a3e1c)"></div></article>
<article class="abs card" style="left:311px"><div class="photo" role="img" aria-label="Performer on stage under violet and red lights" style="background:radial-gradient(circle at 45% 40%,#8a4ae0,#3a1a8a 70%,#5a0a3a)"></div></article>
<article class="abs card" style="left:528px"><div class="photo" role="img" aria-label="Album art of a group in black and white striped outfits" style="background:radial-gradient(circle,#b04050,#2a2a6a 75%)"></div></article>

<div class="abs card-meta" style="left:114px"><span class="name">Lorem Ipsum</span><span class="link">www.penandreel.com</span><span class="desc">Lorem Ipsum is <em>simply dummy text</em></span></div>
<div class="abs card-meta" style="left:331px"><span class="name">Lorem Ipsum</span><span class="link">www.penandreel.com</span><span class="desc">Lorem Ipsum is <em>simply dummy text</em></span></div>
<div class="abs card-meta" style="left:548px"><span class="name">Lorem Ipsum</span><span class="link">www.penandreel.com</span><span class="desc">Lorem Ipsum is <em>simply dummy text</em></span></div>

<div class="abs socials" style="left:100px"><span class="first">Pb</span><span>Ch</span><span>Wc</span><span>Sf</span><span>Tl</span><span>Cs</span><span>Po</span></div>
<div class="abs socials" style="left:323px"><span>Pb</span><span>Ch</span><span>Wc</span><span>Sf</span><span>Tl</span><span>Cs</span><span>Po</span></div>
<div class="abs socials" style="left:541px"><span>Pb</span><span>Ch</span><span>Wc</span><span>Sf</span><span>Tl</span><span>Cs</span><span>Po</span></div>
<div class="abs rule"></div>

<h2 class="abs section-title video-title">VIDEO</h2>
<h2 class="abs section-title bio-title">BIOGRAPHY</h2>

<div class="abs player" role="img" aria-label="Video still of a violinist in black and white">
  <div class="play" style="left:84px;top:49px"><svg width="10" height="12"><path d="M1 0v12l9-6z" fill="#fff"/></svg></div>
  <div class="bar">
    <svg class="abs" style="left:12px;top:4px" width="26" height="8"><path d="M0 0v8l6-4z" fill="#fff"/><path d="M15 2h3l3-2v8l-3-2h-3z" fill="#fff"/></svg>
    <div class="track"><i></i></div>
    <span class="time">11:57</span><span class="hd">HD</span>
    <svg class="abs" style="left:192px;top:4px" width="8" height="8"><path d="M0 8l8-8M4 0h4v4M0 4v4h4" stroke="#fff" fill="none"/></svg>
  </div>
</div>
<div class="abs thumb" role="img" aria-label="Black and white dancer" style="left:95px;background:linear-gradient(140deg,#777,#111)"><div class="play" style="left:20px;top:37px"><svg width="8" height="10"><path d="M0 0v10l8-5z" fill="#fff"/></svg></div></div>
<div class="abs thumb" role="img" aria-label="Guitarist in violet light" style="left:166px;background:linear-gradient(140deg,#3a2a4a,#0a0a0a 60%,#6a3a5a)"><div class="play" style="left:20px;top:37px"><svg width="8" height="10"><path d="M0 0v10l8-5z" fill="#fff"/></svg></div></div>
<div class="abs thumb" role="img" aria-label="Concert crowd under yellow stage lights" style="left:237px;background:radial-gradient(circle at 40% 30%,#ffe23a,#e58a10 60%,#6a2a05)"><div class="play" style="left:20px;top:37px"><svg width="8" height="10"><path d="M0 0v10l8-5z" fill="#fff"/></svg></div></div>

<div class="abs bio-photo" role="img" aria-label="Black and white portrait of the blogger for the biography"></div>
<h3 class="abs about">About Me</h3>
<div class="abs about-text">
  <p>Sed ut perspiciatis unde omnis iste natus error sit voluptatem accusantium doloremque laudantium, totam rem aperiam, eaque ipsa quae ab illo inventore veritatis et quasi architecto beatae vitae dicta sunt explicabo.</p>
  <p>Nemo enim ipsam voluptatem quia voluptas sit aspernatur aut odit aut fugit, sed quia consequuntur magni dolores eos qui ratione voluptatem sequi nesciunt. Neque porro quisquam est, qui dolorem ipsum quia dolor sit amet, consectetur,</p>
  <p class="tight">Sed ut perspiciatis unde omnis iste natus error sit voluptatem accusantium doloremque laudantium, totam rem aperiam, eaque ipsa quae ab illo inventore veritatis et quasi architecto beatae vitae dicta sunt explicabo.</p>
</div>
<div class="abs btn">Read more</div>

<footer class="abs footer"></footer>
<h4 class="abs foot-title" style="left:98px">LATEST NEWS</h4>
<h4 class="abs foot-title" style="left:330px">QUICK LINKS</h4>
<h4 class="abs foot-title" style="left:546px">NEWSLETTER</h4>

<div class="abs news" style="top:1045px"><div class="date"><b>01</b><small>JAN</small></div><h4>HEADDING</h4><p>Lorem Ipsum is simply dummy text of the printing</p></div>
<div class="abs news" style="top:1108px"><div class="date"><b>01</b><small>JAN</small></div><h4>HEADDING</h4><p>Lorem Ipsum is simply dummy text of the printing</p></div>

<ul class="abs links">
  <li>Home</li><li>Biography</li><li>Photos</li><li>Videos</li><li>Blog</li><li>News</li><li>Contact us</li>
</ul>

<div class="abs news-input"></div>
<div class="abs go">GO</div>
<div class="abs subscribe">Subscribe to our newsletter:</div>
<h4 class="abs follow">FOLLOW US</h4>
<div class="abs follow-icons"><span class="first">Ch</span><span>Pb</span><span>C+</span><span>Wl</span></div>
<div class="abs copy">© 2012.www.Velvet&amp;fern.com</div>

</body>
</html>
```